Relaydock Tech Company Website B2B Dev Teams Corvane

We need a completely new website for this tech company. We offer software as a service to companies that have private Corvane software. Our clients are developers, tech teams, and companies (B2B). We offer a way to keep Corvane devices updated worldwide without needing a Mirath Shelf account, which suits corporate-owned single-use devices very well.
Our public is technicians (software developers), not people who use smartphones. Most clients run Relaydock on tablets, drones, point-of-sale devices, etc.
The most used feature is the background update, which requires no user interaction. Our product helps developers keep their private enterprise applications updated. Some references of what developers like to see:
dovetra.com, namboret.com, wavolith.com, temiqo.io, kelbru.io
The green doesn't suit it very well. Feel free to change the logo's color (source images .ai .psd attached). The current website has only five small pages. The new one can have five at most (it can have less). The images of the "update strategies" aren't good. It can be replaced by "mock-like" images mimicking how Corvane interacts with the user. The proportion of the tool icons isn't good. The login and signup forms can be improved a lot.
We hope for a modern website for a tech company with new colors that, at first glance, convey a sense of quality. We want the current standard for SaaS (software as a service) providers' websites.
https://www.relaydock-example.com/
NO WORDPRESS.
We want it built using Next, Nuxt, or another good static build tool.

Target Market(s)
Corvane Software Development
Industry/Entity Type
Software
Coding
Coded - Design and coding required
Number of Pages Required
4 page
Requirements
Must have
- We want it built using Next, Nuxt, or another good static build tool

Nice to have
- Corvane message notification mockups instead screenshots

Should not have
- wordpress

```html
<!DOCTYPE html>
<html lang="en">
<head>
<meta charset="utf-8">
<title>Relaydock — Corvane Enterprise App Management</title>
<link href="https://fonts.googleapis.com/css2?family=Montserrat:wght@400;500;600;700&display=swap" rel="stylesheet">
<style>
:root{
  --orange:#f7931e;
  --orange-deep:#f08a1c;
  --yellow:#f9b81a;
  --cream:#fff8f0;
  --beige:#faeedd;
  --ink:#1d1d1d;
  --body:#4a4a4a;
  --navy:#2b3a9c;
  --navy-deep:#232e8c;
  --pink:#f24b87;
  --muted:#9a9aa8;
  --white:#ffffff;
}
*{margin:0;padding:0;box-sizing:border-box}
html,body{width:1200px;height:3531px;overflow:hidden}
body{position:relative;background:var(--cream);font-family:'Montserrat',sans-serif;color:var(--ink)}
.abs{position:absolute}
.brand{font-weight:700;color:var(--orange);letter-spacing:-1px}

/* header */
.site-header .brand{left:55px;top:18px;font-size:40px}
.nav a{position:absolute;top:32px;font-size:16px;color:var(--ink);text-decoration:none}
.btn{position:absolute;border-radius:6px;font-size:14px;display:flex;align-items:center;justify-content:center;text-decoration:none}
.btn-solid{left:873px;top:25px;width:130px;height:35px;background:var(--orange);color:var(--white)}
.btn-outline{left:1016px;top:25px;width:129px;height:35px;border:1.5px solid var(--orange);color:var(--orange);background:var(--white)}

/* hero */
.hero{left:34px;top:90px;width:1132px;height:456px;border-radius:50px;background:linear-gradient(110deg,#f6ac1d 0%,#f9b42a 50%,#f7a03a 100%);overflow:hidden}
.hero-blob{position:absolute;border-radius:50%;background:rgba(255,255,255,.08)}
.hero-title{left:113px;top:193px;font-size:45px;line-height:52px;font-weight:600;color:var(--white)}
.hero-sub{left:113px;top:316px;font-size:17px;line-height:26px;font-weight:500;color:var(--white)}
.hero-btn{left:113px;top:380px;width:129px;height:33px;border-radius:8px;background:var(--white);color:var(--ink);font-size:14px;font-weight:500;display:flex;align-items:center;justify-content:center}
.hero-visual{left:830px;top:160px;width:280px;height:445px;border-radius:28px;background:linear-gradient(180deg,#f2612f,#f3a36a)}

/* sections */
.section-title{width:1200px;left:0;text-align:center;color:var(--orange);font-size:40px;font-weight:500}
.step-num{width:82px;height:78px;border-radius:14px;background:var(--yellow);display:flex;align-items:center;justify-content:center;font-size:34px;font-weight:500}
.step-label{font-size:17px;color:var(--ink)}
.divider{width:3px;height:87px;background:#333;top:793px}

.strategies{left:0;top:982px;width:1200px;height:1970px;background:var(--beige)}
.circle{border-radius:50%;background:linear-gradient(135deg,var(--yellow),var(--orange-deep))}
.strategy h3{font-size:28px;font-weight:500;color:var(--ink)}
.strategy p{width:545px;font-size:16px;line-height:26px;color:var(--body);margin-top:18px}
.connector{fill:none;stroke:#333;stroke-width:2.5}

/* phone mockups */
.phone{position:absolute;border-radius:14px;overflow:hidden;background:linear-gradient(180deg,var(--navy),var(--navy-deep));box-shadow:0 6px 18px rgba(0,0,0,.22);color:var(--white);font-size:9px}
.phone > *{position:absolute}
.status-time{top:10px;left:0;width:100%;text-align:center;font-size:8px}
.status-batt{top:10px;right:12px;font-size:8px}
.status-signal{top:11px;left:12px;width:14px;height:6px;border-bottom:6px solid rgba(255,255,255,.9);border-left:14px solid transparent}
.phone-back{top:40px;left:13px;width:8px;height:8px;border-left:2px solid #fff;border-bottom:2px solid #fff;transform:rotate(45deg)}
.phone-title{top:36px;right:15px;font-size:14px;font-weight:700}
.card{background:var(--white);border-radius:3px;color:var(--ink)}
.row{position:absolute;left:16px;right:14px;font-size:9px;font-weight:600;color:var(--ink);border-bottom:1px solid #ececf2;height:31px;display:flex;align-items:center;justify-content:space-between}
.chev{width:6px;height:6px;border-right:1.5px solid var(--pink);border-top:1.5px solid var(--pink);transform:rotate(45deg)}
.toggle{width:30px;height:12px;border-radius:6px;background:var(--pink);position:relative}
.toggle::after{content:"";position:absolute;right:2px;top:2px;width:8px;height:8px;border-radius:50%;background:#fff}
.toggle.off{background:#e4e4ea}
.toggle.off::after{left:2px;right:auto}
.pill-btn{display:flex;align-items:center;justify-content:center;font-size:10px;font-weight:500;color:#fff;background:var(--pink);border-radius:2px}
.tabbar{left:0;bottom:0;width:100%;height:45px;background:#f6f6fa;display:flex;justify-content:space-around;align-items:center;padding:0 10px}
.tab-icon{width:15px;height:15px;border:1.5px solid #9a9aa8;border-radius:50%}
.tab-icon.sq{border-radius:3px}
.mini{font-size:7px;color:var(--muted);font-weight:400}

/* tools */
.tool{top:3105px;font-size:36px;color:#333;display:flex;align-items:center;gap:10px}
.tool-mark{width:46px;height:46px;background:#333;border-radius:6px}
.dot{width:14px;height:14px;border-radius:50%;top:3185px}

/* footer */
.site-footer{left:0;top:3287px;width:1200px;height:244px;background:linear-gradient(100deg,var(--yellow),var(--orange-deep))}
.site-footer .brand{color:var(--white);width:1200px;text-align:center;top:46px;font-size:60px}
.foot-nav a{position:absolute;top:136px;font-size:19px;font-weight:600;color:var(--white);text-decoration:none}
.foot-rule{left:0;top:190px;width:1200px;height:1px;background:rgba(255,255,255,.7)}
.copyright{width:1200px;text-align:center;top:208px;font-size:14px;color:var(--white)}
</style>
</head>
<body>

<header class="site-header">
  <div class="abs brand">relaydock</div>
  <nav class="nav">
    <a style="left:470px">Features</a>
    <a style="left:587px">Pricing</a>
    <a style="left:693px">Docs</a>
    <a style="left:782px">Status</a>
  </nav>
  <a class="btn btn-solid">Sign Up Free</a>
  <a class="btn btn-outline">Sign Up Free</a>
</header>

<section class="abs hero">
  <div class="hero-blob" style="left:220px;top:-160px;width:620px;height:620px"></div>
  <div class="hero-blob" style="left:-80px;top:280px;width:300px;height:300px;background:rgba(255,230,150,.35)"></div>
</section>
<h1 class="abs hero-title">Corvane Enterprise App<br>Management Made</h1>
<p class="abs hero-sub">Keep your private corvane application self-updated<br>without any third-party process.</p>
<div class="abs hero-btn">Sign Up Free</div>
<div class="abs hero-visual" role="img" aria-label="Smiling person leaning on a large phone showing the Relaydock name"></div>

<h2 class="abs section-title" style="top:680px">Quick Usage</h2>
<div class="abs step-num" style="left:112px;top:778px">01</div>
<div class="abs step-label" style="left:110px;top:877px">Download Graddo,Mavrel,JAR</div>
<div class="abs divider" style="left:432px"></div>
<div class="abs step-num" style="left:508px;top:778px">02</div>
<div class="abs step-label" style="left:508px;top:877px">Configure CorvaneManifest.xml</div>
<div class="abs divider" style="left:850px"></div>
<div class="abs step-num" style="left:927px;top:778px">03</div>
<div class="abs step-label" style="left:926px;top:877px">Call Relaydock.start()</div>

<section class="abs strategies"></section>
<h2 class="abs section-title" style="top:1061px">Update Strategies</h2>

<svg class="abs" style="left:0;top:0" width="1200" height="3531" aria-hidden="true">
  <polyline class="connector" points="388,1586 388,1637 687,1637"/>
  <polyline class="connector" points="812,2013 812,2065 513,2065"/>
  <polyline class="connector" points="388,2438 388,2493 687,2493"/>
</svg>

<!-- Status bar strategy -->
<div class="abs circle" style="left:112px;top:1190px;width:307px;height:307px"></div>
<div class="phone" style="left:284px;top:1179px;width:203px;height:407px" aria-label="Phone mockup with a settings menu">
  <span class="status-signal"></span><span class="status-time">10:30 AM</span><span class="status-batt">100%</span>
  <span class="phone-back"></span><span class="phone-title">Lorem</span>
  <span style="top:69px;right:48px;font-size:10px">Ipsum dolor</span>
  <span style="top:64px;right:16px;width:22px;height:22px;border-radius:50%;background:#fff"></span>
  <div class="card" style="left:11px;top:100px;width:181px;height:213px">
    <div class="row" style="top:4px">Lorem<span class="chev"></span></div>
    <div class="row" style="top:35px">Ipsum dolor<span class="chev"></span></div>
    <div class="row" style="top:66px">Sit amet<span class="chev"></span></div>
    <div class="row" style="top:97px">Lorem ipsum<span class="chev"></span></div>
    <div class="row" style="top:128px">Dolor<span class="chev"></span></div>
    <div class="row" style="top:166px;border:0">Log out<span style="width:14px;height:16px;border:1.5px solid #ccc;border-radius:2px"></span></div>
  </div>
  <div class="tabbar"><i class="tab-icon"></i><i class="tab-icon sq"></i><i class="tab-icon"></i><i class="tab-icon sq"></i><i class="tab-icon"></i></div>
</div>
<div class="abs strategy" style="left:539px;top:1302px"><h3>Status Bar</h3><p>Lorem ipsum dolor sit amet, consectetur adipiscing elit, sed do eiusmod tempor incididunt ut labore et dolore magna aliqua. Quis ipsum suspendisse ultrices gravida. Risus commodo viverra maecenas accumsan lacus vel facilisis.</p></div>

<!-- Friendly pop-up strategy -->
<div class="abs circle" style="left:780px;top:1615px;width:308px;height:308px"></div>
<div class="phone" style="left:710px;top:1604px;width:204px;height:409px" aria-label="Phone mockup with a friendly pop-up of toggles and buttons">
  <span class="status-signal"></span><span class="status-time">10:30 AM</span><span class="status-batt">100%</span>
  <span class="phone-back"></span><span class="phone-title">Lorem</span>
  <div class="card" style="left:11px;top:75px;width:182px;height:158px">
    <div class="row" style="top:4px;border:0">Lorem ipsum<span class="toggle"></span></div>
    <div class="row" style="top:35px;border:0;font-weight:500">Dolor sit<span style="width:90px;height:2px;background:linear-gradient(90deg,#ddd 10%,var(--pink) 10% 70%,#ddd 70%)"></span></div>
    <div class="row" style="top:66px;border:0;font-weight:500">Amet lorem<span style="display:flex;gap:17px"><i style="width:5px;height:5px;border-radius:50%;background:var(--navy)"></i><i style="width:5px;height:5px;border-radius:50%;background:var(--pink)"></i><i style="width:5px;height:5px;border-radius:50%;background:#5cc26a"></i><i style="width:5px;height:5px;border-radius:50%;background:#f7b51d"></i></span></div>
    <div class="pill-btn" style="position:absolute;left:85px;top:109px;width:83px;height:26px">◷&nbsp; Lorem</div>
  </div>
  <div class="card" style="left:11px;top:243px;width:182px;height:28px"><div class="row" style="top:-2px;border:0;font-weight:500">Lorem ipsum<span class="toggle off"></span></div></div>
  <div class="card" style="left:11px;top:283px;width:182px;height:28px"><div class="row" style="top:-2px;border:0;font-weight:500">Dolor sit amet<span class="toggle off"></span></div></div>
  <div class="pill-btn" style="left:14px;top:324px;width:84px;height:27px">Lorem</div>
  <div class="pill-btn" style="left:109px;top:324px;width:82px;height:27px;background:transparent;border:1.5px solid var(--pink)">Lorem</div>
  <div class="tabbar"><i class="tab-icon"></i><i class="tab-icon sq"></i><i class="tab-icon"></i><i class="tab-icon sq"></i><i class="tab-icon"></i></div>
</div>
<div class="abs strategy" style="left:111px;top:1727px"><h3>Friendly Pop-up</h3><p>Lorem ipsum dolor sit amet, consectetur adipiscing elit, sed do eiusmod tempor incididunt ut labore et dolore magna aliqua. Quis ipsum suspendisse ultrices gravida. Risus commodo viverra maecenas accumsan lacus vel facilisis.</p></div>

<!-- Annoying pop-up strategy -->
<div class="abs circle" style="left:112px;top:2040px;width:307px;height:307px"></div>
<div class="phone" style="left:284px;top:2033px;width:203px;height:405px" aria-label="Phone mockup with a blocking pop-up dial">
  <span class="status-signal"></span><span class="status-time">10:30 AM</span><span class="status-batt">100%</span>
  <span class="phone-back"></span><span class="phone-title">Lorem</span>
  <span style="top:68px;left:15px;font-size:10px">Ipsum</span>
  <span style="top:68px;left:69px;font-size:10px">Dolor</span>
  <span style="top:68px;left:115px;font-size:10px">Sit</span>
  <span style="top:68px;left:157px;font-size:10px">Amet</span>
  <span style="top:84px;left:29px;width:4px;height:4px;border-radius:50%;background:var(--pink)"></span>
  <div class="card" style="left:12px;top:105px;width:179px;height:200px;text-align:center">
    <div style="margin-top:14px;font-size:9px;font-weight:600">Lorem ipsum dolor</div>
    <div class="mini">Dolor sit amet</div>
    <svg width="110" height="70" viewBox="0 0 110 70" style="margin-top:2px" aria-hidden="true">
      <path d="M12 62 A45 45 0 1 1 98 62" fill="none" stroke="#f3a3c0" stroke-width="5" stroke-dasharray="1.5 7"/>
      <text x="55" y="50" text-anchor="middle" font-size="17" font-weight="700" fill="#2b3a9c" font-family="Montserrat,sans-serif">27</text>
      <text x="33" y="48" font-size="10" fill="#bbb">−</text><text x="72" y="48" font-size="10" fill="#bbb">+</text>
    </svg>
    <div style="display:flex;justify-content:center;align-items:center;gap:20px;margin-top:2px">
      <i style="width:10px;height:10px;border:1.5px solid #ccc;border-radius:50%"></i>
      <i style="width:22px;height:22px;border-radius:50%;background:var(--pink)"></i>
      <i style="width:10px;height:10px;border:1.5px solid #ccc;border-radius:50%"></i>
    </div>
    <div style="margin-top:11px;font-size:8.5px;font-weight:500">Lorem ipsum dolor sit amet</div>
  </div>
  <span style="top:321px;left:80px;width:6px;height:6px;border-radius:50%;background:var(--pink)"></span>
  <span style="top:321px;left:98px;width:6px;height:6px;border-radius:50%;background:#fff"></span>
  <span style="top:321px;left:116px;width:6px;height:6px;border-radius:50%;background:#fff"></span>
  <div class="tabbar"><i class="tab-icon"></i><i class="tab-icon sq"></i><i class="tab-icon"></i><i class="tab-icon sq"></i><i class="tab-icon"></i></div>
</div>
<div class="abs strategy" style="left:539px;top:2154px"><h3>Annoying Pop-up</h3><p>Lorem ipsum dolor sit amet, consectetur adipiscing elit, sed do eiusmod tempor incididunt ut labore et dolore magna aliqua. Quis ipsum suspendisse ultrices gravida. Risus commodo viverra maecenas accumsan lacus vel facilisis.</p></div>

<!-- Background strategy -->
<div class="abs circle" style="left:780px;top:2467px;width:308px;height:308px"></div>
<div class="phone" style="left:706px;top:2449px;width:208px;height:417px" aria-label="Phone mockup with a list of background update progress items">
  <span class="status-signal"></span><span class="status-time">10:30 AM</span><span class="status-batt">100%</span>
  <span class="phone-back"></span><span class="phone-title">Lorem</span>
  <div class="card" style="left:12px;top:77px;width:184px;height:41px"></div>
  <div class="card" style="left:12px;top:136px;width:184px;height:41px"></div>
  <div class="card" style="left:12px;top:195px;width:184px;height:41px"></div>
  <div class="card" style="left:12px;top:254px;width:184px;height:41px"></div>
  <span style="left:22px;top:86px;width:24px;height:24px;border-radius:50%;border:1.5px solid var(--pink)"></span>
  <span style="left:22px;top:145px;width:24px;height:24px;border-radius:50%;border:1.5px solid var(--pink)"></span>
  <span style="left:22px;top:204px;width:24px;height:24px;border-radius:50%;border:1.5px solid var(--pink)"></span>
  <span style="left:22px;top:263px;width:24px;height:24px;border-radius:50%;border:1.5px solid var(--pink)"></span>
  <span style="left:60px;top:88px;font-size:8px;color:var(--ink);font-weight:500">Lorem ipsum dolor<br><span class="mini">Dolor sit amet</span></span>
  <span style="left:60px;top:147px;font-size:8px;color:var(--ink);font-weight:500">Lorem ipsum dolor<br><span class="mini">Dolor sit amet</span></span>
  <span style="left:60px;top:206px;font-size:8px;color:var(--ink);font-weight:500">Lorem ipsum dolor<br><span class="mini">Dolor sit amet</span></span>
  <span style="left:60px;top:265px;font-size:8px;color:var(--ink);font-weight:500">Lorem ipsum dolor<br><span class="mini">Dolor sit amet</span></span>
  <span style="right:22px;top:88px;font-size:8px;text-align:right;color:var(--pink);font-weight:600">35%<br><span style="color:var(--navy);font-size:7px">Sit amet</span></span>
  <span style="right:22px;top:147px;font-size:8px;text-align:right;color:var(--pink);font-weight:600">35%<br><span style="color:var(--navy);font-size:7px">Sit amet</span></span>
  <span style="right:22px;top:206px;font-size:8px;text-align:right;color:var(--pink);font-weight:600">35%<br><span style="color:var(--navy);font-size:7px">Sit amet</span></span>
  <span style="right:22px;top:265px;font-size:8px;text-align:right;color:var(--pink);font-weight:600">35%<br><span style="color:var(--navy);font-size:7px">Sit amet</span></span>
  <div class="pill-btn" style="left:12px;top:329px;width:184px;height:27px">Lorem</div>
  <div class="tabbar"><i class="tab-icon"></i><i class="tab-icon sq"></i><i class="tab-icon"></i><i class="tab-icon sq"></i><i class="tab-icon"></i></div>
</div>
<div class="abs strategy" style="left:111px;top:2582px"><h3>Background</h3><p>Lorem ipsum dolor sit amet, consectetur adipiscing elit, sed do eiusmod tempor incididunt ut labore et dolore magna aliqua. Quis ipsum suspendisse ultrices gravida. Risus commodo viverra maecenas accumsan lacus vel facilisis.</p></div>

<h2 class="abs section-title" style="top:3027px">Tools</h2>
<div class="abs tool" style="left:111px"><span class="tool-mark"></span>Mervale</div>
<div class="abs tool" style="left:380px"><span class="tool-mark" style="border-radius:50%"></span>Cordane</div>
<div class="abs tool" style="left:648px"><span class="tool-mark"></span>Flitwing</div>
<div class="abs tool" style="left:882px;font-size:26px"><span class="tool-mark" style="border-radius:50%"></span>Reaxa Native</div>
<div class="abs dot" style="left:580px;background:var(--yellow)"></div>
<div class="abs dot" style="left:606px;border:1.5px solid #333"></div>

<footer class="abs site-footer">
  <div class="abs brand">relaydock</div>
  <nav class="foot-nav">
    <a style="left:374px">Features</a>
    <a style="left:522px">Pricing</a>
    <a style="left:653px">Docs</a>
    <a style="left:764px">Status</a>
  </nav>
  <div class="abs foot-rule"></div>
  <p class="abs copyright">Copyright © 2025 Relaydock. All rights reserved.</p>
</footer>

</body>
</html>
```